Business Card Design for boarding house accomodation business

I need a business card design for my Sydney based boarding house business accomodation. providing rooms for rent in Sydney Australia with shard bathroom and kitchen.
The front of card, are my details with details of head office and the rear of card to have details of locations providing rooms for rent.

Industry/Entity Type

Business

Contact Information for Business Card

Front of card details:
HOLLOWAY MANAGEMENT PTY LTD t/a
LINDFIELD'S GUEST HOUSE
ABN:52907318460
Daniel Kavanagh
48 Clement st
Newtown 2042
Mobile:0417386920
Email:daniel@lindfieldsguesthouse.example.au

Back of Card:
Locations:
-48 Clement st
Newtown 2042

-362 Harlow st
Erskineville 2043

-87 Fenwick st
Bondi 2026

-294 Ashcombe rd
Marrickville 2043

```html
<!DOCTYPE html>
<html lang="en">
<head>
<meta charset="utf-8">
<title>Holloway Management – Business Card</title>
<link href="https://fonts.googleapis.com/css2?family=Jost:wght@500;700&family=Lato:wght@400;700&display=swap" rel="stylesheet">
<style>
  :root {
    --bg: #2b2d31;
    --card: #ffffff;
    --ink: #1e1e1e;
    --muted: #6b6b6b;
    --green: #3aa12a;
    --green-light: #7cc242;
    --faint: #ececec;
    --rule: #bdbdbd;
  }
  * { box-sizing: border-box; margin: 0; padding: 0; }
  html, body { width: 1200px; height: 864px; overflow: hidden; }
  body {
    background: var(--bg);
    font-family: "Lato", Arial, sans-serif;
    color: var(--ink);
    position: relative;
  }
  .card {
    position: absolute;
    left: 320px;
    width: 560px;
    height: 320px;
    background: var(--card);
    overflow: hidden;
    box-shadow: 0 10px 30px rgba(0,0,0,.35);
  }
  .card--back { top: 92px; }
  .card--front { top: 452px; }

  .brand { font-family: "Jost", Arial, sans-serif; }
  .brand__name {
    font-weight: 700;
    font-size: 22px;
    letter-spacing: .5px;
    color: var(--ink);
    white-space: nowrap;
  }
  .brand__tagline {
    display: flex;
    align-items: center;
    gap: 8px;
    font-weight: 500;
    font-size: 11px;
    letter-spacing: .6px;
    color: var(--muted);
    margin-top: 1px;
  }
  .brand__tagline::before,
  .brand__tagline::after {
    content: "";
    flex: 1;
    height: 1px;
    background: var(--rule);
  }

  /* back side */
  .back__mark {
    position: absolute; left: 253px; top: 22px;
    width: 54px; height: 54px; border-radius: 50%;
    background: linear-gradient(180deg, var(--green-light), var(--green));
  }
  .back__disc {
    position: absolute; left: 380px; top: 40px;
    width: 300px; height: 300px; border-radius: 50%;
    background: var(--faint);
  }
  .back .brand { position: absolute; left: 0; right: 0; top: 86px; text-align: center; }
  .back .brand__tagline { width: 360px; margin: 1px auto 0; }
  .locations__title {
    position: absolute; left: 0; right: 0; top: 150px;
    text-align: center;
    font-family: "Jost", Arial, sans-serif;
    font-weight: 500; font-size: 18px; letter-spacing: 1px;
    color: var(--green);
  }
  .locations {
    position: absolute; top: 186px; left: 60px; right: 40px;
    display: grid; grid-template-columns: 1fr 1fr; column-gap: 28px; row-gap: 12px;
    font-size: 13px; line-height: 1.25;
  }
  .location { display: flex; align-items: flex-start; gap: 6px; }
  .location--left { justify-content: flex-end; text-align: right; }
  .icon { width: 12px; height: 14px; flex: none; margin-top: 2px; fill: var(--green); }

  /* front side */
  .front__disc {
    position: absolute; left: 330px; top: 60px;
    width: 360px; height: 360px; border-radius: 50%;
    background: linear-gradient(180deg, var(--green-light), var(--green) 70%);
  }
  .front .brand { position: absolute; left: 34px; top: 26px; width: 350px; }
  .front .brand__tagline { padding-left: 40px; }
  .contact { position: absolute; left: 40px; top: 130px; font-size: 14px; }
  .contact__name {
    font-weight: 700; font-size: 20px; color: var(--green); margin-bottom: 12px;
  }
  .contact__row { display: flex; align-items: center; gap: 8px; margin-bottom: 6px; }
  .contact__label { font-weight: 700; color: var(--green); }
  .contact__address { margin-top: 6px; }
</style>
</head>
<body>

  <section class="card card--back back" aria-label="Card back: locations">
    <div class="back__disc"></div>
    <div class="back__mark"></div>
    <div class="brand">
      <div class="brand__name">HOLLOWAY MANAGEMENT PTY LTD</div>
      <div class="brand__tagline">LINDFIELD'S GUEST HOUSE</div>
    </div>
    <h2 class="locations__title">LOCATIONS</h2>
    <div class="locations">
      <div class="location location--left">
        <span>362 Harlow st<br>Erskineville 2043</span>
        <svg class="icon" viewBox="0 0 12 14"><path d="M6 0a5 5 0 0 0-5 5c0 3.6 5 9 5 9s5-5.4 5-9a5 5 0 0 0-5-5zm0 7a2 2 0 1 1 0-4 2 2 0 0 1 0 4z"/></svg>
      </div>
      <div class="location">
        <svg class="icon" viewBox="0 0 12 14"><path d="M6 0a5 5 0 0 0-5 5c0 3.6 5 9 5 9s5-5.4 5-9a5 5 0 0 0-5-5zm0 7a2 2 0 1 1 0-4 2 2 0 0 1 0 4z"/></svg>
        <span>48 Clement st<br>Newtown 2042</span>
      </div>
      <div class="location location--left">
        <span>294 Ashcombe rd<br>Marrickville 2043</span>
        <svg class="icon" viewBox="0 0 12 14"><path d="M6 0a5 5 0 0 0-5 5c0 3.6 5 9 5 9s5-5.4 5-9a5 5 0 0 0-5-5zm0 7a2 2 0 1 1 0-4 2 2 0 0 1 0 4z"/></svg>
      </div>
      <div class="location">
        <svg class="icon" viewBox="0 0 12 14"><path d="M6 0a5 5 0 0 0-5 5c0 3.6 5 9 5 9s5-5.4 5-9a5 5 0 0 0-5-5zm0 7a2 2 0 1 1 0-4 2 2 0 0 1 0 4z"/></svg>
        <span>87 Fenwick st<br>Bondi 2026</span>
      </div>
    </div>
  </section>

  <section class="card card--front front" aria-label="Card front: contact details">
    <div class="front__disc"></div>
    <div class="brand">
      <div class="brand__name">HOLLOWAY MANAGEMENT PTY LTD</div>
      <div class="brand__tagline">LINDFIELD'S GUEST HOUSE</div>
    </div>
    <div class="contact">
      <div class="contact__name">Daniel Kavanagh</div>
      <div class="contact__row"><span class="contact__label">ABN:</span> 52907318460</div>
      <div class="contact__row">
        <svg class="icon" viewBox="0 0 12 12"><path d="M2.4 0 4.5 2.6 3.4 4a7 7 0 0 0 4.6 4.6l1.4-1.1L12 9.6 10.6 12C5 12 0 7 0 1.4z"/></svg>
        0417386920
      </div>
      <div class="contact__row">
        <svg class="icon" viewBox="0 0 12 10"><path d="M0 0h12v1.2L6 5 0 1.2zM0 2.6l6 3.8 6-3.8V10H0z"/></svg>
        daniel@lindfieldsguesthouse.example.au
      </div>
      <div class="contact__address">48 Clement st Newtown 2042</div>
    </div>
  </section>

</body>
</html>
```